Business Card Design and Logo Needed

I need Business Cards and a Logo for my website and public speaking business which can be found at: www.kelsa-thorn.example

I'm looking for creative and unique ideas. Some business cards I've found online that I like can be found at:
http://gigplatelo.example/general/18-smokin-hot-business-card-designs/

and at

http://www.vortaplume.example/2009/04/50-creative-business-cards-of-50-graphic-designers/

```html
<!DOCTYPE html>
<html lang="en">
<head>
<meta charset="utf-8">
<title>Kelsa Thorn – Business Card</title>
<link rel="stylesheet" href="https://fonts.googleapis.com/css2?family=Questrial&family=Great+Vibes&display=swap">
<style>
  :root {
    --card-bg: #ffffff;
    --role-speaker: #66e22c;
    --role-philanthropist: #1f5cf2;
    --role-author: #8a22e2;
    --name-ink: #111111;
  }
  html, body {
    margin: 0;
    padding: 0;
    overflow: hidden;
    background: var(--card-bg);
  }
  .card {
    position: relative;
    width: 781px;
    height: 1200px;
    background: var(--card-bg);
    overflow: hidden;
  }
  .roles {
    position: absolute;
    left: 50px;
    top: 250px;
    margin: 0;
    padding: 0;
    list-style: none;
    font-family: "Questrial", "Century Gothic", sans-serif;
    font-size: 84px;
    line-height: 110px;
    letter-spacing: 0.5px;
  }
  .roles__speaker { color: var(--role-speaker); }
  .roles__philanthropist { color: var(--role-philanthropist); }
  .roles__author { color: var(--role-author); }
  .card__name {
    position: absolute;
    left: 0;
    right: 0;
    top: 835px;
    margin: 0;
    text-align: center;
    font-family: "Great Vibes", cursive;
    font-weight: 400;
    font-size: 126px;
    line-height: 1;
    color: var(--name-ink);
  }
</style>
</head>
<body>
  <main class="card">
    <ul class="roles">
      <li class="roles__speaker">Speaker</li>
      <li class="roles__philanthropist">Philanthropist</li>
      <li class="roles__author">Author</li>
    </ul>
    <h1 class="card__name">Kelsa Thorn</h1>
  </main>
</body>
</html>
```